VELVET RUMBA/New Packaging Design

We need a new packaging design for our product. We are looking a fresh image and something that catches attention from the consumer.

Velvet Rumba is a mix of selected dried peppers and sugar.

Our company name is Brelodan, we own the brand Vopri, we have offices in Mexico & United States. www.brelodan.example www.vopri.example

```html
<!DOCTYPE html>
<html lang="en">
<head>
<meta charset="utf-8">
<title>Vopri Velvet Rumba – Pouch Front</title>
<link href="https://fonts.googleapis.com/css2?family=Bangers&family=Fira+Sans+Condensed:wght@300;400&display=swap" rel="stylesheet">
<style>
  :root {
    --backdrop: #f2f2f2;
    --gold: #d9a21e;
    --gold-dark: #c88d12;
    --band: #fbb514;
    --band-light: #ffd21a;
    --red: #c4151c;
    --red-deep: #7c0c0f;
    --chili: #e8202a;
    --leaf: #1f9a3c;
    --ink: #1b1b1b;
    --white: #ffffff;
  }
  * { margin: 0; padding: 0; box-sizing: border-box; }
  html, body { width: 1200px; height: 1200px; overflow: hidden; background: var(--backdrop); }
  .canvas { position: relative; width: 1200px; height: 1200px; display: flex; align-items: center; justify-content: center; }
  .pouch-front {
    position: relative; width: 600px; height: 1000px;
    background: linear-gradient(180deg, var(--gold) 0%, var(--gold-dark) 100%);
    border-radius: 18px; overflow: hidden;
    font-family: "Fira Sans Condensed", sans-serif;
  }
  .pouch-front svg.backdrop-shapes { position: absolute; inset: 0; }
  .brand-lockup {
    position: absolute; top: 110px; left: 210px; width: 180px;
    display: flex; flex-direction: column; align-items: center; gap: 14px;
  }
  .brand-dot { width: 80px; height: 80px; border-radius: 50%; background: var(--leaf); }
  .brand-name { font-family: "Fira Sans Condensed", sans-serif; font-weight: 300; font-size: 52px; color: var(--ink); line-height: 1; }
  .product-title {
    position: absolute; top: 320px; left: 110px; width: 380px;
    font-family: "Bangers", cursive; font-weight: 400; font-size: 108px; line-height: 0.86;
    color: var(--red); text-align: center; transform: rotate(-4deg);
    -webkit-text-stroke: 3px var(--ink); paint-order: stroke fill;
    text-shadow: 5px 5px 0 var(--white), -5px -5px 0 var(--white), 5px -5px 0 var(--white), -5px 5px 0 var(--white), 0 7px 0 var(--white), 0 -7px 0 var(--white), 7px 0 0 var(--white), -7px 0 0 var(--white);
  }
  .flavour { position: absolute; top: 560px; left: 140px; width: 220px; text-align: center; color: var(--white); z-index: 2; }
  .flavour-name { font-size: 32px; font-weight: 400; letter-spacing: -0.5px; line-height: 1.1; }
  .flavour-tagline { font-size: 18px; font-weight: 300; line-height: 1.3; margin-top: 6px; letter-spacing: -0.3px; }
  .chili-art {
    position: absolute; top: 700px; left: 110px; width: 470px; height: 200px;
    border-radius: 50% 40% 45% 55% / 55% 45% 50% 45%;
    background: radial-gradient(ellipse at 55% 45%, var(--chili) 0%, #d41a22 60%, #a5121a 100%);
  }
  .net-weight { position: absolute; bottom: 42px; left: 0; width: 600px; text-align: center; font-size: 17px; font-weight: 300; color: var(--white); letter-spacing: -0.3px; z-index: 2; }
</style>
</head>
<body>
<main class="canvas">
  <section class="pouch-front">
    <svg class="backdrop-shapes" viewBox="0 0 600 1000" width="600" height="1000" aria-hidden="true">
      <defs>
        <radialGradient id="red-field" cx="0.45" cy="0.6" r="0.7">
          <stop offset="0" stop-color="#e01d24"/>
          <stop offset="0.6" stop-color="#b3141a"/>
          <stop offset="1" stop-color="#7c0c0f"/>
        </radialGradient>
        <linearGradient id="band-fill" x1="0" y1="0" x2="0" y2="1">
          <stop offset="0" stop-color="#fbb514"/>
          <stop offset="0.5" stop-color="#ffd21a"/>
          <stop offset="1" stop-color="#f7a114"/>
        </linearGradient>
      </defs>
      <path d="M600 60 C 330 130, 110 390, 90 700 C 80 880, 200 960, 350 960 C 460 960, 540 930, 600 880 Z" fill="url(#band-fill)"/>
      <path d="M600 140 C 380 200, 180 420, 150 700 C 135 860, 240 930, 350 930 C 450 930, 530 900, 600 850 Z" fill="url(#red-field)"/>
    </svg>

    <div class="brand-lockup">
      <span class="brand-dot"></span>
      <span class="brand-name">Vopri</span>
    </div>

    <h1 class="product-title">VELVET RUMBA</h1>

    <div class="flavour">
      <p class="flavour-name">PICANTE</p>
      <p class="flavour-tagline">Heat Up Snack Time With<br>The Perfect Blend of<br>Spicy and Sweet</p>
    </div>

    <div class="chili-art" role="img" aria-label="Illustration of three glossy red chili peppers with green stems"></div>

    <p class="net-weight">NET WT 5.3 OZ (150 g)</p>
  </section>
</main>
</body>
</html>
```